Criação de Papelaria Profissional para Consultoria de Negócios
A empresa queria:
" Serviços de Consultoria de Carreira (transição, desenvolvimento de liderança), Assessment, Coaching, Outplacement, Headhunting "

```html
<!DOCTYPE html>
<html lang="pt-BR">
<head>
<meta charset="utf-8">
<title>Livia Moretti – Consultoria de Carreira</title>
<link href="https://fonts.googleapis.com/css2?family=Cormorant+Garamond:wght@400;500&family=Open+Sans:wght@400;600&display=swap" rel="stylesheet">
<style>
  :root {
    --page-bg: #efece8;
    --wine-dark: #3f0a0f;
    --wine: #6b141c;
    --wine-light: #8a2029;
    --ink-light: #ffffff;
    --ink-soft: #e9d6d8;
    --bar-grey: #c9c9cb;
    --photo-light: #f4f4f4;
    --photo-mid: #d9dadc;
    --photo-dark: #5a5d63;
  }
  * { margin: 0; padding: 0; box-sizing: border-box; }
  html, body {
    width: 1200px; height: 1200px; overflow: hidden;
    background: var(--page-bg);
  }
  .canvas { position: relative; width: 1200px; height: 1200px; }

  .profile-tile {
    position: absolute; left: 463px; top: 199px;
    width: 269px; height: 269px;
    background: radial-gradient(circle at 40% 40%, var(--wine-light), var(--wine) 55%, var(--wine-dark));
    display: flex; align-items: center; justify-content: center;
  }
  .profile-name {
    font-family: "Cormorant Garamond", serif;
    font-weight: 400; font-size: 30px; letter-spacing: 2px;
    color: var(--ink-light); text-transform: uppercase;
  }

  .cover {
    position: absolute; left: 65px; top: 504px;
    width: 1068px; height: 415px; overflow: hidden;
  }
  .cover-photo {
    position: absolute; inset: 0;
    background:
      radial-gradient(ellipse at 35% 60%, var(--photo-light) 0%, transparent 60%),
      linear-gradient(100deg, var(--photo-mid) 0%, var(--photo-light) 35%, var(--photo-mid) 55%, var(--photo-dark) 75%);
  }
  .cover-shape { position: absolute; inset: 0; }

  .brand-name {
    position: absolute; left: 690px; top: 140px;
    font-family: "Cormorant Garamond", serif;
    font-weight: 400; font-size: 50px; line-height: 1;
    color: var(--ink-light); text-transform: uppercase; letter-spacing: 1px;
  }
  .brand-rule {
    position: absolute; left: 692px; top: 196px;
    width: 252px; height: 1px; background: var(--ink-soft);
  }
  .brand-tagline {
    position: absolute; left: 692px; top: 202px;
    font-family: "Cormorant Garamond", serif;
    font-size: 16px; letter-spacing: 4.3px;
    color: var(--ink-soft); text-transform: uppercase;
  }

  .contact-list {
    position: absolute; left: 690px; top: 286px;
    font-family: "Open Sans", sans-serif; font-size: 13px; line-height: 17px;
    color: var(--ink-light); list-style: none;
  }
  .contact-item { display: flex; align-items: center; gap: 12px; margin-bottom: 7px; }
  .contact-icon { width: 16px; height: 16px; flex: none; }

  .footer-bar {
    position: absolute; left: 691px; top: 384px;
    width: 364px; height: 24px; border-radius: 3px;
    background: linear-gradient(180deg, #e2e2e4, var(--bar-grey));
  }
</style>
</head>
<body>
<main class="canvas">
  <section class="profile-tile">
    <span class="profile-name">Livia Moretti</span>
  </section>

  <section class="cover">
    <div class="cover-photo" role="img" aria-label="Fotografia de mãos com canetas revisando documentos sobre uma mesa de reunião"></div>
    <svg class="cover-shape" viewBox="0 0 1068 415" width="1068" height="415" aria-hidden="true">
      <defs>
        <radialGradient id="wineFill" cx="0.35" cy="0.45" r="0.8">
          <stop offset="0" stop-color="#8a2029"/>
          <stop offset="0.55" stop-color="#5e1118"/>
          <stop offset="1" stop-color="#3f0a0f"/>
        </radialGradient>
      </defs>
      <path d="M660 0 C 610 110, 615 280, 650 415 L 1068 415 L 1068 0 Z" fill="url(#wineFill)"/>
    </svg>

    <h1 class="brand-name">Livia Moretti</h1>
    <div class="brand-rule"></div>
    <p class="brand-tagline">Consultoria de Carreira</p>

    <ul class="contact-list">
      <li class="contact-item">
        <svg class="contact-icon" viewBox="0 0 16 16"><path d="M4 1.5 L6.5 4.5 L5 6.3 C6 8.3 7.7 10 9.7 11 L11.5 9.5 L14.5 12 L13 14.5 C7 14.5 1.5 9 1.5 3 Z" fill="#fff"/></svg>
        <span>00 0000.0000<br>00 0000.0000</span>
      </li>
      <li class="contact-item">
        <svg class="contact-icon" viewBox="0 0 16 16"><circle cx="8" cy="8" r="6.5" fill="none" stroke="#fff" stroke-width="1.4"/><path d="M1.5 8 H14.5 M8 1.5 C5 5 5 11 8 14.5 M8 1.5 C11 5 11 11 8 14.5" fill="none" stroke="#fff" stroke-width="1.1"/></svg>
        <span>MORETTICARREIRA.COM.BR<br>CONTATO@MORETTICARREIRA.COM.BR</span>
      </li>
    </ul>

    <div class="footer-bar"></div>
  </section>
</main>
</body>
</html>
```